Presentation folder for holding wedding cake literature

We need to have a front cover design as well as a back cover design for a presentation folder to hold literature for a bakery who sells a lot of wedding cakes.

We have uploaded a couple copies of ideas that we like. They are for demonstrative purposes only.

The text on the front cover needs to be:
-The Frosting Parlor-
-Designing, baking and decorating perfect wedding cakes...Guaranteed!

On the back cover it needs to say:
-Serving VELVETcrumb cakes and a "Silver Ribbon" Experience-

In addition the back cover must contain the "Silver Ribbon Baker" logo.

We will only supply photos if necessary. We would rather have you choose them.

We are open to any colors as long as they are soft.

For a reference of the client, go to http://www.brindlefrostingparlor.example

Target Market(s)

The target market is primarily women ages 25-40.

Industry/Entity Type

Wedding

Requirements
Must have
• Must have priorities are listed in the brief.
Nice to have
• Fonts should be a combination of "script" and one or more complementary styles.

Colors should be either a soft blue, pinkish tone or lavender tone. Mixing any of the colors with a light gray would be acceptable as well.
Should not have
• No dark colors such as black, red, purple, green or orange.

```html
<!DOCTYPE html>
<html lang="en">
<head>
<meta charset="utf-8">
<title>The Frosting Parlor – Presentation Folder</title>
<link rel="stylesheet" href="https://fonts.googleapis.com/css2?family=Cinzel:wght@400&family=Pinyon+Script&family=Open+Sans:wght@400;600&display=swap">
<style>
  :root {
    --backdrop: #c9c3bf;
    --folder-blue: #5cc6d3;
    --icing-white: #ffffff;
    --cake-light: #f4f2ee;
    --cake-shade: #d9d6d0;
  }
  * { box-sizing: border-box; margin: 0; padding: 0; }
  html, body {
    width: 1200px; height: 857px; overflow: hidden;
    background: var(--backdrop);
  }
  .folder-spread { position: relative; width: 1200px; height: 857px; }
  .cover {
    position: absolute; top: 108px; width: 480px; height: 640px;
    background: var(--folder-blue);
    overflow: hidden;
    box-shadow: 0 6px 18px rgba(0,0,0,0.18);
  }
  .cover--front { left: 70px; }
  .cover--back { left: 650px; }

  .title-band {
    position: absolute; left: 0; width: 100%; height: 108px;
    border-top: 8px solid var(--icing-white);
    border-bottom: 8px solid var(--icing-white);
  }
  .front-title-band { top: 62px; }
  .back-title-band { top: 44px; }

  .brand-title {
    position: absolute; left: 0; right: 0; top: 26px;
    text-align: center;
    font-family: "Cinzel", serif;
    font-weight: 400;
    font-size: 36px; letter-spacing: 2px;
    color: var(--icing-white);
  }
  .brand-title .small-cap { font-size: 27px; }

  .front-tagline {
    position: absolute; left: 30px; top: 200px; width: 210px;
    font-family: "Pinyon Script", cursive;
    font-size: 28px; line-height: 40px;
    color: var(--icing-white);
  }

  .cake-photo {
    position: absolute; left: 262px; top: 182px; width: 218px; height: 458px;
    background: linear-gradient(100deg, var(--cake-shade) 0%, var(--cake-light) 35%, var(--icing-white) 60%, var(--cake-shade) 100%);
  }

  .guarantee-seal {
    position: absolute; left: 210px; top: 440px; width: 146px; height: 146px;
    border-radius: 50%;
    background: var(--icing-white);
    padding: 6px;
  }
  .guarantee-seal__inner {
    width: 100%; height: 100%; border-radius: 50%;
    background: var(--folder-blue);
    border: 2px dashed var(--icing-white);
    display: flex; align-items: center; justify-content: center;
    font-family: "Pinyon Script", cursive;
    font-size: 20px; color: var(--icing-white);
  }

  .back-tagline {
    position: absolute; left: 66px; top: 30px;
    font-family: "Open Sans", sans-serif;
    font-size: 15px; line-height: 19px;
    color: var(--icing-white);
  }

  .baker-mark {
    position: absolute; left: 150px; top: 500px;
    display: flex; align-items: center; gap: 10px;
  }
  .baker-mark__dot {
    width: 24px; height: 24px; border-radius: 50%;
    background: var(--icing-white);
  }
  .baker-mark__name {
    font-family: "Open Sans", sans-serif;
    font-size: 20px; font-weight: 600;
    color: var(--icing-white);
  }
</style>
</head>
<body>
<main class="folder-spread">

  <section class="cover cover--front" aria-label="Front cover">
    <div class="title-band front-title-band">
      <h1 class="brand-title">T<span class="small-cap">HE</span> F<span class="small-cap">ROSTING</span> P<span class="small-cap">ARLOR</span></h1>
    </div>

    <p class="front-tagline">Designing, baking and decorating perfect wedding cakes...</p>

    <div class="cake-photo" role="img" aria-label="Photo of a white tiered wedding cake with silver ribbons and white roses on top"></div>

    <div class="guarantee-seal">
      <div class="guarantee-seal__inner">Guaranteed!</div>
    </div>
  </section>

  <section class="cover cover--back" aria-label="Back cover">
    <div class="title-band back-title-band">
      <p class="back-tagline">Serving VELVETcrumb cakes<br>and a "Silver Ribbon" Experience</p>
    </div>

    <div class="baker-mark">
      <span class="baker-mark__dot"></span>
      <span class="baker-mark__name">Silver Ribbon Baker</span>
    </div>
  </section>

</main>
</body>
</html>
```